Business Card Design for new consultancy company

Name of Company: Orbit Lanternway
Nature of Business: Digital Business Consultancy
Specialises in Digital Media Strategy, Digital Business Model Transformation, Over-The-Top (OTT) Development, Web Business Development, Digital Marketing, Web and App Product Development, Design and Innovation

Website: http://www.orbit-lanternway.example

Designs can be of any colour or any number of colours, objective is to give the impression we are a digital trend setter, creative and impactful.

Also please suggest a logo to complement the name and business card.

Target Market(s)

Media Companies, Telcos, Enterprises

Industry/Entity Type

Business

Contact Information for Business Card

Standard business card size. OK with to play with small variations like corners for impact/impression.

Font styles to use
Serif
Sans Serif

Requirements
Must have
• Clarity, Impact, Creativity
Nice to have
• Design should encapsulate professionalism, expertise, yet trend-setting and vibrant for digital consultancy
Should not have
• Messy layout, too gaudy colours or design

```html
<!DOCTYPE html>
<html lang="en">
<head>
<meta charset="utf-8">
<title>Orbit Lanternway – Business Card</title>
<link rel="stylesheet" href="https://fonts.googleapis.com/css2?family=Libre+Baskerville:wght@400;700&family=PT+Serif:wght@400;700&display=swap">
<style>
  :root {
    --page-bg: #e9e6e1;
    --card-white: #fbfbfa;
    --card-grey: #ececea;
    --ink: #1b1b1b;
    --ink-soft: #4a4a4a;
    --rule: #9a9a9a;
    --band: #111111;
    --band-text: #f4f4f4;
  }
  html, body {
    margin: 0;
    padding: 0;
    width: 1200px;
    height: 818px;
    overflow: hidden;
    background: var(--page-bg);
  }
  .card {
    position: absolute;
    left: 100px;
    top: 124px;
    width: 1000px;
    height: 570px;
    background: linear-gradient(160deg, var(--card-white) 40%, var(--card-grey) 100%);
    box-shadow: 0 10px 30px rgba(0,0,0,0.18);
    font-family: "PT Serif", serif;
    color: var(--ink);
  }
  .brand {
    position: absolute;
    left: 70px;
    top: 150px;
    width: 400px;
  }
  .brand-name {
    display: flex;
    align-items: center;
    gap: 16px;
    font-family: "Libre Baskerville", serif;
    font-size: 40px;
    font-weight: 400;
    letter-spacing: 1px;
    text-transform: uppercase;
    line-height: 1.1;
    color: var(--ink);
  }
  .brand-square {
    width: 26px;
    height: 26px;
    background: var(--ink);
    flex: none;
  }
  .brand-rule {
    height: 1px;
    background: var(--rule);
    margin: 14px 0 10px;
  }
  .brand-tagline {
    font-family: "Libre Baskerville", serif;
    font-size: 16px;
    letter-spacing: 3px;
    text-transform: uppercase;
    color: var(--ink-soft);
  }
  .divider {
    position: absolute;
    left: 520px;
    top: 70px;
    width: 1px;
    height: 300px;
    background: linear-gradient(to bottom, transparent, var(--rule) 20%, var(--rule) 80%, transparent);
  }
  .contact {
    position: absolute;
    left: 580px;
    top: 75px;
  }
  .person-name {
    font-family: "Libre Baskerville", serif;
    font-size: 30px;
    letter-spacing: 1px;
    text-transform: uppercase;
    margin: 0;
  }
  .person-role {
    font-size: 18px;
    color: var(--ink-soft);
    margin: 4px 0 44px;
  }
  .contact-list {
    list-style: none;
    margin: 0;
    padding: 0;
  }
  .contact-item {
    display: flex;
    align-items: center;
    gap: 12px;
    font-size: 22px;
    margin-bottom: 10px;
  }
  .contact-icon {
    width: 22px;
    height: 22px;
    flex: none;
  }
  .specialties-band {
    position: absolute;
    left: 0;
    right: 0;
    bottom: 0;
    height: 165px;
    background: var(--band);
    color: var(--band-text);
    display: flex;
    flex-direction: column;
    justify-content: center;
    align-items: center;
    text-align: center;
    font-size: 20px;
    line-height: 1.55;
  }
  .specialties-band p { margin: 0; }
</style>
</head>
<body>
  <div class="card">
    <div class="brand">
      <div class="brand-name"><span class="brand-square"></span><span>Orbit Lanternway</span></div>
      <div class="brand-rule"></div>
      <div class="brand-tagline">Digital Business Consultancy</div>
    </div>

    <div class="divider"></div>

    <div class="contact">
      <h1 class="person-name">Marcus Hale</h1>
      <div class="person-role">Managing Director</div>
      <ul class="contact-list">
        <li class="contact-item">
          <svg class="contact-icon" viewBox="0 0 22 22" aria-hidden="true">
            <rect width="22" height="22" fill="#1b1b1b"/>
            <path d="M6 5h3l1 3-2 1.5a9 9 0 0 0 4.5 4.5L14 12l3 1v3a1 1 0 0 1-1 1A11 11 0 0 1 5 6a1 1 0 0 1 1-1z" fill="#fff"/>
          </svg>
          <span>0098 7654 321</span>
        </li>
        <li class="contact-item">
          <svg class="contact-icon" viewBox="0 0 22 22" aria-hidden="true">
            <rect width="22" height="22" fill="#1b1b1b"/>
            <rect x="4" y="6" width="14" height="10" fill="none" stroke="#fff" stroke-width="1.5"/>
            <path d="M4 6l7 6 7-6" fill="none" stroke="#fff" stroke-width="1.5"/>
          </svg>
          <span>info@orbit-lanternway.example</span>
        </li>
        <li class="contact-item">
          <svg class="contact-icon" viewBox="0 0 22 22" aria-hidden="true">
            <rect width="22" height="22" fill="#1b1b1b"/>
            <circle cx="11" cy="11" r="6.5" fill="none" stroke="#fff" stroke-width="1.3"/>
            <ellipse cx="11" cy="11" rx="3" ry="6.5" fill="none" stroke="#fff" stroke-width="1.1"/>
            <path d="M4.5 11h13M5.5 8h11M5.5 14h11" stroke="#fff" stroke-width="1"/>
          </svg>
          <span>www.orbit-lanternway.example</span>
        </li>
      </ul>
    </div>

    <div class="specialties-band">
      <p>Specialises in Digital Media Strategy, Digital Business Model Transformation</p>
      <p>Over-The-Top (OTT) Development, Web Business Development</p>
      <p>Digital Marketing, Web and App Product Development, Design and Innovation</p>
    </div>
  </div>
</body>
</html>
```